Construction Website Design for Wordpress

Update:
I like this theme as a starting point. It seems like a very good start. Fonts, colors, motion, etc. https://advisory.kelbrowthemes.com/
***************************************************************************************

I want a new website design that can be implemented in wordpress. Here is my existing site: www.vantornmeasures.com
Attached is a document with the copy, requirements, sample images, etc. Let me know what questions you have.

Here is a sample of the info, but review the attached document for everything:

Website layout:
Title Bar
• Home
• Expertise
• Takeoffs
• Divisions Serviced (redesign from orig page: (http://www.vantornmeasures.com/scope-list/)
• Member Login
Requirements
• Home page has a slider with 3 dimmed commercial construction images and copy overlay
• Request for Proposal Form should be over the slider and the same look and location on every page.
• “Request For Proposal” – No Obligation
o Company Name
o Contact Name
o Contact Phone
o Contact Email
• Use the copy below for the pages
• Split the Client Testimonials among the pages

Target Market(s)

B2B - Construction Companies

Industry/Entity Type

Construction

Number of Pages Required

4 page

Font styles to use
Serif

Colors
0255a3
3276b5
85abd2
d0dfed

Requirements
Must have
• Construction images in slider
• Request for proposal form
• testimonials

```html
<!DOCTYPE html>
<html lang="en">
<head>
<meta charset="utf-8">
<title>Vantorn Measures – Commercial Construction Takeoff Experts</title>
<link rel="stylesheet" href="https://fonts.googleapis.com/css2?family=Roboto:wght@300;400;500;700&display=swap">
<style>
  :root {
    --navy: #0b2034;
    --navy-deep: #081a2b;
    --brand: #0255a3;
    --brand-mid: #3276b5;
    --brand-light: #85abd2;
    --brand-pale: #d0dfed;
    --accent: #1f8fd6;
    --accent-bright: #3aa0e6;
    --ink: #1b1b1b;
    --muted: #4a4a4a;
    --field-line: #c9d3dc;
    --grey-band: #efefef;
    --base-bar: #222629;
    --white: #ffffff;
  }
  * { box-sizing: border-box; margin: 0; padding: 0; }
  html, body {
    width: 960px; height: 1200px; overflow: hidden;
    background: var(--white);
    font-family: "Roboto", Arial, sans-serif;
  }
  .site {
    position: absolute; left: 159px; top: 0;
    width: 762px; height: 1424px;
    transform: scale(0.8427); transform-origin: top left;
    background: var(--white);
    box-shadow: 0 0 10px rgba(0,0,0,.25);
  }
  .abs { position: absolute; }

  /* Hero */
  .hero-photo {
    left: 246px; top: 0; width: 516px; height: 337px;
    background: linear-gradient(160deg, #2b7fc8 0%, #1a5fa6 40%, #0f3f78 75%, #123a5e 100%);
  }
  .hero-panel { left: 0; top: 0; width: 246px; height: 337px; background: var(--navy); }
  .brand-name {
    left: 55px; top: 22px; font-size: 12px; font-weight: 400;
    letter-spacing: 1px; color: var(--accent-bright);
  }
  .brand-name::before {
    content: ""; display: inline-block; width: 7px; height: 7px;
    background: var(--accent-bright); margin-right: 6px; vertical-align: 1px;
  }
  .main-nav { left: 416px; top: 18px; display: flex; align-items: center; }
  .main-nav a {
    color: var(--white); text-decoration: none; font-size: 7px; font-weight: 300;
    letter-spacing: .3px; padding: 4px 8px;
  }
  .main-nav a.login { background: var(--brand); margin-left: 4px; padding: 4px 7px; }
  .hero-kicker { left: 64px; top: 148px; color: var(--white); font-size: 14px; font-weight: 400; }
  .hero-title {
    left: 64px; top: 176px; color: var(--white); font-size: 25px;
    font-weight: 700; line-height: 31px;
  }
  .slider-dots { left: 62px; top: 314px; display: flex; gap: 2px; }
  .slider-dots span { width: 11px; height: 11px; border-radius: 50%; border: 1px solid var(--accent-bright); }
  .slider-dots span.on { background: var(--accent-bright); }

  /* Proposal band */
  .proposal-band { left: 0; top: 337px; width: 762px; height: 73px; background: var(--brand); }
  .proposal-title { left: 61px; top: 350px; color: #3c92dc; font-size: 25px; font-weight: 300; }
  .proposal-sub { left: 64px; top: 379px; color: var(--white); font-size: 12.5px; font-weight: 400; }
  .proposal-arrow { left: 154px; top: 386px; }

  .proposal-form {
    left: 421px; top: 221px; width: 284px; height: 279px;
    background: var(--white); border-radius: 12px;
    box-shadow: 0 2px 8px rgba(0,0,0,.2);
  }
  .field {
    position: absolute; left: 32px; width: 218px; height: 34px;
    border: 1px solid var(--field-line); font-size: 7px; color: #8a949c;
    padding: 13px 9px; font-family: inherit;
  }
  .submit-btn {
    position: absolute; left: 32px; top: 212px; width: 110px; height: 26px;
    border: 1px solid var(--accent); color: var(--brand-mid);
    font-size: 11px; text-align: center; line-height: 24px; letter-spacing: .5px;
  }

  /* Testimonial */
  .testimonial-quote {
    left: 64px; top: 452px; width: 312px; font-size: 10.5px;
    line-height: 14px; color: var(--ink);
  }
  .testimonial-name { left: 64px; top: 514px; font-size: 13.5px; color: var(--brand-mid); }

  /* Video band */
  .video-photo {
    left: 3px; top: 590px; width: 381px; height: 206px;
    background: linear-gradient(120deg, #2a6eaa 0%, #1d5590 45%, #2d7bc0 70%, #15406e 100%);
  }
  .video-panel { left: 384px; top: 590px; width: 378px; height: 206px; background: var(--navy); }
  .video-lead {
    left: 429px; top: 634px; color: var(--white); font-size: 18px;
    font-weight: 300; line-height: 23px;
  }
  .video-link { left: 429px; top: 727px; color: var(--accent-bright); font-size: 20px; font-weight: 300; }
  .video-play { left: 653px; top: 725px; }

  /* Process */
  .process-visual {
    left: 73px; top: 852px; width: 293px; height: 303px;
    background: linear-gradient(180deg, #dfe5eb 0%, #c7ced5 100%);
  }
  .process-kicker { left: 408px; top: 865px; font-size: 14px; color: var(--muted); }
  .process-title { left: 404px; top: 885px; font-size: 26px; font-weight: 700; color: #1a7fc4; }
  .process-steps { left: 405px; top: 938px; width: 318px; list-style: none; }
  .process-steps li {
    position: relative; padding-left: 19px; font-size: 10.5px;
    line-height: 14px; color: var(--ink); margin-bottom: 14px;
  }
  .process-steps li .num {
    position: absolute; left: 0; top: 1px; width: 11px; height: 11px;
    border-radius: 50%; background: var(--accent); color: var(--white);
    font-size: 7px; line-height: 11px; text-align: center; font-weight: 500;
  }

  /* Call to action */
  .cta-band { left: 0; top: 1155px; width: 762px; height: 137px; background: var(--grey-band); }
  .cta-lead { left: 73px; top: 1205px; font-size: 14px; font-weight: 500; color: var(--ink); }
  .cta-sub { left: 73px; top: 1230px; font-size: 17px; font-weight: 300; color: var(--accent); }
  .cta-btn {
    left: 559px; top: 1219px; width: 109px; height: 24px; background: var(--accent);
    color: var(--white); font-size: 11px; text-align: center; line-height: 24px; letter-spacing: .5px;
  }

  /* Footer */
  .site-footer { left: 0; top: 1292px; width: 762px; height: 113px; background: var(--navy-deep); }
  .footer-brand { left: 68px; top: 1326px; font-size: 11px; letter-spacing: 1px; color: var(--accent-bright); }
  .footer-brand::before {
    content: ""; display: inline-block; width: 6px; height: 6px;
    background: var(--accent-bright); margin-right: 6px; vertical-align: 1px;
  }
  .footer-col { top: 1313px; }
  .footer-col h4 { font-size: 10.5px; font-weight: 400; color: var(--brand-mid); margin-bottom: 8px; letter-spacing: .3px; }
  .footer-col p { font-size: 11.5px; line-height: 14px; color: var(--white); }
  .footer-social { font-size: 13px; font-weight: 700; color: var(--white); }
  .base-bar { left: 0; top: 1405px; width: 762px; height: 19px; background: var(--base-bar); }
  .base-bar p { position: absolute; left: 300px; top: 5px; font-size: 7px; color: var(--accent-bright); }
</style>
</head>
<body>
<div class="site">

  <header>
    <div class="abs hero-photo" role="img" aria-label="Dimmed blue photo of commercial steel-frame construction against the sky"></div>
    <div class="abs hero-panel"></div>
    <div class="abs brand-name">VANTORN MEASURES</div>
    <nav class="abs main-nav">
      <a href="#">HOME</a><a href="#">EXPERTISE</a><a href="#">TAKEOFFS</a><a href="#">DIVISIONS SERVICED</a><a href="#" class="login">MEMBER LOGIN</a>
    </nav>
    <p class="abs hero-kicker">EXPERIENCED</p>
    <h1 class="abs hero-title">Commercial Construction<br>Takeoff Experts</h1>
    <div class="abs slider-dots"><span class="on"></span><span></span><span></span></div>
  </header>

  <section>
    <div class="abs proposal-band"></div>
    <h2 class="abs proposal-title">Request For Proposal</h2>
    <p class="abs proposal-sub">No Obligation</p>
    <svg class="abs proposal-arrow" width="232" height="6" viewBox="0 0 232 6">
      <line x1="0" y1="3" x2="229" y2="3" stroke="#ffffff" stroke-width="0.8"/>
      <path d="M226 1 L230 3 L226 5" fill="none" stroke="#ffffff" stroke-width="0.8"/>
    </svg>

    <form class="abs proposal-form">
      <div class="field" style="top:37px">Company Name</div>
      <div class="field" style="top:79px">Contact Name</div>
      <div class="field" style="top:122px">Contact Phone</div>
      <div class="field" style="top:164px">Email</div>
      <div class="submit-btn">SUBMIT</div>
    </form>

    <p class="abs testimonial-quote">Lorem ipsum dolor sit amet, consectetuer adipiscing elit, sed diam nonummy nibh euismod tincidunt ut laoreet dolore magna aliquam erat volutpat. Ut wisi enim ad minim veniam, quis nostrud exerci tation ullamcorper suscipit lobortis nisl ut</p>
    <p class="abs testimonial-name">John Doe</p>
  </section>

  <section>
    <div class="abs video-photo" role="img" aria-label="Blue double-exposure photo of a construction worker with hard hat over an industrial plant"></div>
    <div class="abs video-panel"></div>
    <p class="abs video-lead">See How We Can Help You<br>In UNDER 60 Seconds!!!</p>
    <p class="abs video-link">INTRODUCTION VIDEO</p>
    <svg class="abs video-play" width="30" height="30" viewBox="0 0 30 30">
      <circle cx="15" cy="15" r="14.5" fill="#1f8fd6"/>
      <path d="M11 8 L22 15 L11 22 Z" fill="#0b2034"/>
    </svg>
  </section>

  <section>
    <div class="abs process-visual" role="img" aria-label="Image of a desktop monitor showing the online project submission form"></div>
    <p class="abs process-kicker">HOW WE WORK</p>
    <h2 class="abs process-title">The Process Is So Easy!</h2>
    <ol class="abs process-steps">
      <li><span class="num">1</span>Click on the button to REGISTER your company.</li>
      <li><span class="num">2</span>Click on "Add Project" to start your first project.</li>
      <li><span class="num">3</span>Give your project a name, load a detailed description of what you want us to do (scope) and load blueprints (or a URL link for us to retrieve the plans.</li>
      <li><span class="num">4</span>Within 24 hours, we will review your blueprints and send you back a FREE QUOTE to complete the work for you.</li>
      <li><span class="num">5</span>You have NO OBLIGATION to continue!</li>
    </ol>
  </section>

  <section>
    <div class="abs cta-band"></div>
    <p class="abs cta-lead">We Can Help You Bid And WIN More Projects!</p>
    <p class="abs cta-sub">so REGISTER and start your first project today!</p>
    <div class="abs cta-btn">REGISTER</div>
  </section>

  <footer>
    <div class="abs site-footer"></div>
    <div class="abs footer-brand">VANTORN MEASURES</div>
    <div class="abs footer-col" style="left:268px">
      <h4>CONTACT INFO</h4>
      <p>Vantorn Measures<br>PO Box 418<br>Brookvale, GA 30174</p>
    </div>
    <div class="abs footer-col" style="left:421px">
      <h4>IMPORTANT LINKS</h4>
      <p>Contact Us<br>Become A Member<br>Sitemap</p>
    </div>
    <div class="abs footer-col" style="left:573px">
      <h4>FOLLOW US</h4>
      <p class="footer-social">ProNet</p>
    </div>
    <div class="abs base-bar"><p>2019 - All Rights Reserved &nbsp;|&nbsp; Vantorn Measures</p></div>
  </footer>

</div>
</body>
</html>
```